Home Page Design

We are refreshing our website and need someone to design a very clean modern home page. We have a wireframe for the content and basic layout (see attached). We just need someone to make it look beautiful.

This web page will be hosted on a private server using HTML5. I have developers who will integrate the rotating images and referenced video files - we just need you to focus on the visual elements.

You can take a look at our current website at tavenfold.com for color style guides, logos, etc.

```html
<!DOCTYPE html>
<html lang="en">
<head>
<meta charset="utf-8">
<title>Tavenfold — Home</title>
<link href="https://fonts.googleapis.com/css2?family=Roboto:wght@300;400&display=swap" rel="stylesheet">
<style>
  :root {
    --brand-blue: #1f5fad;
    --action-green: #7ed23f;
    --white: #ffffff;
    --ink: #1c1c1c;
    --ink-soft: #333333;
  }
  * { margin: 0; padding: 0; box-sizing: border-box; }
  html, body { width: 1200px; height: 1200px; overflow: hidden; }
  body { position: relative; font-family: "Roboto", "Helvetica Neue", Arial, sans-serif; font-weight: 300; background: var(--white); }
  .band { position: absolute; left: 0; width: 1200px; }
  .band--analytics { top: 0; height: 524px; background: var(--brand-blue); color: var(--white); }
  .band--managed { top: 524px; height: 521px; background: var(--white); color: var(--ink-soft); }
  .band--customers { top: 1045px; height: 155px; background: var(--brand-blue); color: var(--white); overflow: hidden; }
  .section-title { position: absolute; font-size: 32px; font-weight: 300; letter-spacing: 0.2px; line-height: 1; }
  .band--managed .section-title { color: var(--ink); }
  .feature-list { position: absolute; list-style: none; font-size: 14.6px; line-height: 27.5px; }
  .feature-list li { position: relative; padding-left: 9px; }
  .feature-list li::before { content: "."; position: absolute; left: 0; top: 0; }
  .cta { position: absolute; width: 130px; height: 35px; border-radius: 4px; background: var(--action-green); color: var(--white); font-size: 13px; font-weight: 400; display: flex; align-items: center; justify-content: center; text-decoration: none; }
  .photo { position: absolute; width: 495px; height: 330px; }
  .photo--laptop { left: 618px; top: 101px; background: linear-gradient(135deg, #c9ab86 0%, #e9dcc8 45%, #b79c7a 100%); }
  .photo--headset { left: 82px; top: 101px; background: linear-gradient(120deg, #f4f4f4 0%, #e8d3c3 50%, #cfe2f2 100%); }
  .photo--customers { left: 618px; top: 97px; height: 330px; background: linear-gradient(180deg, #e9e6e0 0%, #8a8a86 100%); }
</style>
</head>
<body>
  <section class="band band--analytics">
    <h2 class="section-title" style="left:134px; top:98px;">Advanced Cost Analytics</h2>
    <ul class="feature-list" style="left:127px; top:145px;">
      <li>Access to detailed billing records</li>
      <li>Customizable drill down invoice templates</li>
      <li>Nimbus tag integration</li>
      <li>Comprehensive invoice variance analysis</li>
      <li>Side by side Stratus pricing comparisons</li>
      <li>Stratus total cost of ownership</li>
      <li>Spending trends</li>
      <li>Cost forecasting</li>
    </ul>
    <a class="cta" href="#" style="left:134px; top:387px;">Learn More</a>
    <div class="photo photo--laptop" role="img" aria-label="Photo of a smiling woman working on a laptop in a bright office"></div>
  </section>

  <section class="band band--managed">
    <div class="photo photo--headset" role="img" aria-label="Photo of a support agent wearing a headset"></div>
    <h2 class="section-title" style="left:721px; top:98px;">Managed Services</h2>
    <ul class="feature-list" style="left:712px; top:138px;">
      <li>Outsource cost optimization to the experts</li>
      <li>Customized solutions that fit your environment</li>
      <li>Dedicated team of Certified Nimbus Engineers and<br>financial analysts</li>
      <li>Continuous monitoring of your Nimbus environment</li>
      <li>Deep analysis of Nimbus useoge data and billing activity</li>
      <li>Regular meetings to review trends, anomalies and<br>cost saving opportunities</li>
      <li>Detailed analysis of your monthly invoice with<br>comprehensive variance analysis</li>
    </ul>
    <a class="cta" href="#" style="left:723px; top:431px;">Learn More</a>
  </section>

  <section class="band band--customers">
    <h2 class="section-title" style="left:132px; top:97px;">Listen to Our Customers!</h2>
    <div class="photo photo--customers" role="img" aria-label="Photo of a modern café interior with pendant lamps"></div>
  </section>
</body>
</html>
```